Movie Poster "Pickles Past Noonday"

To create a fun, stand out, professional poster. To make people want to click on it.

The movie is a comedy, mockumentary.

You can view trailer on FLTQ.

Movie Story in short, a filmmaker trying to make a movie which is turns out to be a nightmere.

Long Story:
Pickles Past Noonday is a fly on the wall mockumentary following Derek Fallow, a struggling low-budget filmmaker, on his mission to complete his first big-break movie Marigold before the opening premiere. Derek soon finds himself in turmoil as he races against the clock in a make or break scenario packed with side-splitting and nail-biting moments. Will Derek finish in enough time with all the odds stacked up against him?

The movie has won Harwick Gold Prize and got good reviews (please dont put this on poster)

You dont need to use any of the photos provided.

Sick

Sick

Industry/Entity Type

movie

Other font styles liked:
• impact

Requirements
Must have
• bold, easy to read
Should not have
• horror

```html
<!DOCTYPE html>
<html lang="en">
<head>
<meta charset="utf-8">
<title>Pickles Past Noonday — Poster</title>
<link rel="stylesheet" href="https://fonts.googleapis.com/css2?family=Anton&family=Jost:wght@700&display=swap">
<style>
  :root {
    --poster-yellow: #fde00a;
    --film-black: #1e1e1c;
    --title-red: #e30613;
    --beam-white: #ffffff;
    --page-white: #ffffff;
  }
  html, body {
    margin: 0;
    padding: 0;
    width: 938px;
    height: 1200px;
    overflow: hidden;
    background: var(--page-white);
  }
  .poster {
    display: block;
    width: 938px;
    height: 1200px;
  }
  .panel { fill: var(--poster-yellow); }
  .film-band { fill: var(--film-black); }
  .sprocket { fill: var(--poster-yellow); }
  .projector-beam { fill: var(--beam-white); }
  .title-main, .title-sub {
    font-family: "Anton", Impact, sans-serif;
    fill: var(--title-red);
  }
  .tagline {
    font-family: "Jost", "Futura", sans-serif;
    font-weight: 700;
    font-size: 17px;
    letter-spacing: 4.5px;
    fill: var(--film-black);
  }
</style>
</head>
<body>
<svg class="poster" viewBox="0 0 938 1200" xmlns="http://www.w3.org/2000/svg">
  <defs>
    <linearGradient id="camera-tone" x1="0" y1="0" x2="0" y2="1">
      <stop offset="0" stop-color="#c8262a"/>
      <stop offset="0.55" stop-color="#2a2421"/>
      <stop offset="1" stop-color="#e8741a"/>
    </linearGradient>
  </defs>

  <!-- yellow poster field -->
  <rect class="panel" x="104" y="74" width="738" height="1044"/>

  <!-- projector light beam -->
  <polygon class="projector-beam" points="842,262 592,376 593,459 842,592"/>

  <!-- top film strip -->
  <g class="film-strip film-strip--top">
    <rect class="film-band" x="104" y="70" width="742" height="108"/>
    <g class="sprockets">
      <rect class="sprocket" x="140" y="102" width="36" height="63" rx="9"/>
      <rect class="sprocket" x="212" y="102" width="36" height="63" rx="9"/>
      <rect class="sprocket" x="284" y="102" width="36" height="63" rx="9"/>
      <rect class="sprocket" x="356" y="102" width="36" height="63" rx="9"/>
      <rect class="sprocket" x="428" y="102" width="36" height="63" rx="9"/>
      <rect class="sprocket" x="500" y="102" width="36" height="63" rx="9"/>
      <rect class="sprocket" x="572" y="102" width="36" height="63" rx="9"/>
      <rect class="sprocket" x="644" y="102" width="36" height="63" rx="9"/>
      <rect class="sprocket" x="716" y="102" width="36" height="63" rx="9"/>
      <rect class="sprocket" x="788" y="102" width="36" height="63" rx="9"/>
    </g>
  </g>

  <!-- film camera on tripod over flames -->
  <rect class="camera-artwork" x="334" y="251" width="224" height="507" rx="6"
        fill="url(#camera-tone)" role="img"
        aria-label="Illustration of a vintage film camera with red reels on a tripod, flames burning at its feet"/>

  <!-- title -->
  <text class="title-main" x="231" y="872" font-size="128" textLength="487" lengthAdjust="spacingAndGlyphs">PICKLES</text>
  <text class="title-sub" x="231" y="930" font-size="69" textLength="487" lengthAdjust="spacingAndGlyphs">PAST NOONDAY</text>

  <!-- tagline -->
  <text class="tagline" x="229" y="981">LIGHTS...</text>
  <text class="tagline" x="398" y="981">CAMERA...</text>
  <text class="tagline" x="582" y="981">DISASTER.</text>

  <!-- bottom film strip -->
  <g class="film-strip film-strip--bottom">
    <rect class="film-band" x="104" y="1018" width="742" height="102"/>
    <g class="sprockets">
      <rect class="sprocket" x="126" y="1044" width="36" height="63" rx="9"/>
      <rect class="sprocket" x="198" y="1044" width="36" height="63" rx="9"/>
      <rect class="sprocket" x="270" y="1044" width="36" height="63" rx="9"/>
      <rect class="sprocket" x="342" y="1044" width="36" height="63" rx="9"/>
      <rect class="sprocket" x="414" y="1044" width="36" height="63" rx="9"/>
      <rect class="sprocket" x="486" y="1044" width="36" height="63" rx="9"/>
      <rect class="sprocket" x="558" y="1044" width="36" height="63" rx="9"/>
      <rect class="sprocket" x="630" y="1044" width="36" height="63" rx="9"/>
      <rect class="sprocket" x="702" y="1044" width="36" height="63" rx="9"/>
      <rect class="sprocket" x="774" y="1044" width="36" height="63" rx="9"/>
    </g>
  </g>
</svg>
</body>
</html>
```